Oversized Post Card for Busines Owners 1st 2nd and 3rd prizes

Create a professional, fresh and polished oversized post card for law firm specializing in Business Law, Succession Planning, and Employment Law

Use any picture(s) of your choice (mine or ones you recommend), logo, headshot and company info

www.morvenashlegal.example

Greyhill Office - 4172 Copperleaf Drive, Suite 830, Charlotte, NC 28214
Westbrook Office - 18530 Birchmont Way, Suite 410, Charlotte, NC 28263

Phone (704) 555-0187

Use this card for a Free Consultation

Target Market(s)

Business Owners (of small businesses)

Industry/Entity Type

Business

Font styles to use
Serif
Sans Serif

Requirements
Must have
• Company name, logo and contact info
• Serving business owners with legal guidance
• Business Law, Succession Planning & Wealth Transfers
• www.morvenashlegal.example
• Greyhill Office - 4172 Copperleaf Drive, Suite 830, Charlotte, NC 28214
• Westbrook Office - 18530 Birchmont Way, Suite 410, Charlotte, NC 28263
• Phone (704) 555-0187
• Use this card for a Free Consultation
Nice to have
• pictures (yours or mine) - you choose; headshot picture

```html
<!DOCTYPE html>
<html lang="en">
<head>
<meta charset="utf-8">
<title>Morven Ash Legal – Oversized Postcard</title>
<link href="https://fonts.googleapis.com/css2?family=Oswald:wght@400;500&family=Roboto+Condensed:wght@400;700&display=swap" rel="stylesheet">
<style>
  :root{
    --navy:#10243a;
    --ink:#1b2a3a;
    --blue-deep:#0f4a6e;
    --blue:#1f6f99;
    --blue-light:#6cc3ec;
    --band-blue:#2a7eb0;
    --dark-band:#141c27;
    --paper:#ffffff;
    --muted:#cfd7df;
    --stage:#ece9e4;
  }
  *{margin:0;padding:0;box-sizing:border-box}
  html,body{width:1200px;height:1000px;overflow:hidden;background:var(--stage)}
  body{position:relative;font-family:"Roboto Condensed",Arial,sans-serif;color:var(--ink)}

  .card{position:absolute;background:var(--paper);overflow:hidden}
  .card--front{left:46px;top:28px;width:716px;height:459px}
  .card--back{left:438px;top:510px;width:714px;height:461px}

  .front-art{position:absolute;left:0;top:0;width:716px;height:408px}

  .brand{position:absolute;left:28px;top:24px;display:flex;align-items:center;gap:14px}
  .brand__dot{width:72px;height:72px;border-radius:50%;background:var(--blue-deep)}
  .brand__name{font-family:"Oswald",sans-serif;font-weight:400;font-size:27px;color:var(--blue-deep);line-height:1.05}

  .pitch{position:absolute;left:14px;width:250px;text-align:center;color:var(--paper)}
  .pitch__headline{top:138px;font-family:"Oswald",sans-serif;font-weight:500;font-size:21px;line-height:1.2;letter-spacing:.2px}
  .pitch__rule{position:absolute;left:40px;top:196px;width:198px;border-top:2px dotted rgba(255,255,255,.8)}
  .pitch__services{top:203px;font-size:15px;line-height:1.2}

  .headshot{position:absolute;left:89px;top:244px;width:100px;height:100px;border-radius:50%;
    background:radial-gradient(circle at 50% 45%,#e6c9a8 0%,#c9a27a 45%,#7a5a45 100%);border:2px solid rgba(255,255,255,.85)}
  .attorney{position:absolute;left:14px;top:340px;width:250px;text-align:center;color:var(--paper)}
  .attorney__firm{font-weight:700;font-size:13px}
  .attorney__creds{font-size:10px;line-height:1.25}

  .front-footer{position:absolute;left:0;top:408px;width:716px;height:51px;display:flex;align-items:center;justify-content:center;
    font-size:19px;color:var(--navy);gap:10px}
  .front-footer__sep{width:2px;height:24px;background:var(--navy)}

  .back-band{position:absolute;left:0;top:0;width:714px;height:200px;background:var(--dark-band)}
  .bulbs{position:absolute;left:0;top:0;width:300px;height:200px;
    background:radial-gradient(circle at 100px 95px,#f4f6d8 0%,#7fa9c7 12%,#24405a 38%,#111a26 75%)}
  .back-intro{position:absolute;left:313px;top:26px;width:232px}
  .back-intro__firm{font-family:"Oswald",sans-serif;font-weight:400;font-size:15px;color:#a9d6ee;margin-bottom:8px}
  .back-intro__text{font-size:10.5px;line-height:1.42;color:var(--muted)}
  .stamp-box{position:absolute;left:598px;top:10px;width:105px;height:105px;background:var(--paper)}

  .back-brand{position:absolute;left:0;top:215px;width:308px;text-align:center}
  .back-brand__dot{width:72px;height:72px;border-radius:50%;background:var(--blue-deep);margin:0 auto 10px}
  .back-brand__name{font-family:"Oswald",sans-serif;font-weight:400;font-size:23px;color:var(--blue-deep);letter-spacing:.5px}
  .back-brand__contact{margin-top:10px;font-size:10px;font-weight:700;color:var(--ink);display:flex;justify-content:center;gap:8px;align-items:center}
  .back-brand__contact svg{width:9px;height:9px;vertical-align:-1px;margin-right:2px}
  .back-brand__web{font-size:10px;font-weight:700;color:var(--ink);margin-top:3px}

  .offer{position:absolute;left:0;top:397px;width:308px;height:64px;background:var(--band-blue);text-align:center;padding-top:12px}
  .offer__lead{font-family:"Oswald",sans-serif;font-size:12px;color:var(--paper)}
  .offer__main{font-family:"Oswald",sans-serif;font-weight:500;font-size:21px;color:var(--blue-light);letter-spacing:.6px;line-height:1.1}

  .offices{position:absolute;left:313px;top:228px;width:260px}
  .office{margin-bottom:16px;font-size:11px;line-height:1.35;color:var(--ink)}
  .office__firm{font-weight:700;font-size:12px;color:var(--navy)}
</style>
</head>
<body>

<section class="card card--front" aria-label="Postcard front">
  <svg class="front-art" viewBox="0 0 716 408" aria-hidden="false">
    <defs>
      <linearGradient id="panelBlue" x1="0" y1="0" x2="1" y2="1">
        <stop offset="0" stop-color="#2b7fae"/>
        <stop offset="1" stop-color="#0d3d5e"/>
      </linearGradient>
      <linearGradient id="familyTones" x1="0" y1="0" x2="1" y2="1">
        <stop offset="0" stop-color="#6fa9c9"/>
        <stop offset=".45" stop-color="#c9b49a"/>
        <stop offset="1" stop-color="#e9eef0"/>
      </linearGradient>
    </defs>
    <rect width="716" height="408" fill="url(#panelBlue)"/>
    <path d="M0 0 H345 C300 70 190 118 0 128 Z" fill="#ffffff"/>
    <path role="img" aria-label="Photo of a smiling family of four outdoors under a blue sky"
          d="M345 0 H716 V408 H238 C262 300 290 140 345 0 Z" fill="url(#familyTones)"/>
  </svg>

  <div class="brand">
    <div class="brand__dot"></div>
    <div class="brand__name">Morven Ash<br>Legal PLLC</div>
  </div>

  <h1 class="pitch pitch__headline">SERVING BUSINESS OWNERS<br>WITH LEGAL GUIDANCE</h1>
  <div class="pitch__rule"></div>
  <p class="pitch pitch__services">Business Law, Succession<br>Planning &amp; Wealth Transfers</p>

  <div class="headshot" role="img" aria-label="Headshot of the attorney"></div>
  <div class="attorney">
    <p class="attorney__firm">Morven Ash Legal, PLLC</p>
    <p class="attorney__creds">Estate Planning Attorney, CPA<br>Board Certified Specialist in Estate<br>Planning and Probate Law</p>
  </div>

  <div class="front-footer">
    <span>www.morvenashlegal.example</span>
    <span class="front-footer__sep"></span>
    <span>call (704) 555-0187</span>
  </div>
</section>

<section class="card card--back" aria-label="Postcard back">
  <div class="back-band"></div>
  <div class="bulbs" role="img" aria-label="Photo of a row of light bulbs with one glowing"></div>

  <div class="back-intro">
    <h2 class="back-intro__firm">Morven Ash Legal, PLLC</h2>
    <p class="back-intro__text">Serving clients in estate planning, estate administration, probate law, wills, revocable trusts, irrevocable trusts, powers of attorney, health care, powers of attorney, living wills, hipaa releases, guardianships, special needs planning, wealth transfers, elder law and business law in North Carolina and South Carolina.</p>
  </div>
  <div class="stamp-box"></div>

  <div class="back-brand">
    <div class="back-brand__dot"></div>
    <div class="back-brand__name">MORVEN ASH LEGAL, PLLC</div>
    <div class="back-brand__contact">
      <span><svg viewBox="0 0 10 10"><circle cx="5" cy="5" r="4.4" fill="none" stroke="#1f6f99"/><path d="M3.3 2.8 L4.2 2.6 L4.6 3.8 L4 4.3 Q4.5 5.4 5.6 6 L6.1 5.4 L7.3 5.8 L7.1 6.8 Q4.5 7 3.3 2.8Z" fill="#1f6f99"/></svg>(704) 555-0187</span>
      <span>|</span>
      <span><svg viewBox="0 0 10 10"><rect x="1" y="2.5" width="8" height="5.5" fill="none" stroke="#1f6f99"/><path d="M1 2.5 L5 5.6 L9 2.5" fill="none" stroke="#1f6f99"/></svg>morven@morvenashlegal.example</span>
    </div>
    <div class="back-brand__web">www.morvenashlegal.example</div>
  </div>

  <div class="offer">
    <p class="offer__lead">USE THIS CARD FOR A</p>
    <p class="offer__main">FREE CONSULTATION</p>
  </div>

  <div class="offices">
    <address class="office" style="font-style:normal">
      <div class="office__firm">Morven Ash Legal, PLLC</div>
      Greyhill Office<br>4172 Copperleaf Drive, Suite 830<br>Charlotte, NC 28214
    </address>
    <address class="office" style="font-style:normal">
      <div class="office__firm">Morven Ash Legal, PLLC</div>
      Westbrook Office<br>18530 Birchmont Way, Suite 410<br>Charlotte, NC 28263
    </address>
  </div>
</section>

</body>
</html>
```